Business card design for online Mandarin Learning School

We need a business card design for our online language learning school called "Sunny Kite Academy for Mandarin Learning". Our existing website is https://www.sunnykiteacademy.com
We have our logo already. We would like to see our business card design that can make our online teaching services to be innovative, young, energetic and fun to learn. Prefer to have a certain level of color matching with our website. Apart from "Sunny Kite Academy", need to specifically state "for Mandarin Learning" as well on the business card.

```html
<!DOCTYPE html>
<html lang="en">
<head>
<meta charset="UTF-8">
<title>Sunny Kite Academy – Business Card</title>
<link href="https://fonts.googleapis.com/css2?family=Marcellus&family=Montserrat:wght@600&family=Roboto:wght@400&display=swap" rel="stylesheet">
<style>
  :root {
    --backdrop: #2b2c2e;
    --card: #1f2021;
    --card-edge: #2a2b2c;
    --emboss: #161718;
    --emboss-light: #2c2d2f;
    --teal: #21a0ac;
    --coral: #e0605e;
    --white: #f4f4f4;
    --grey-text: #d6d6d6;
  }
  * { margin: 0; padding: 0; box-sizing: border-box; }
  html, body {
    width: 1200px; height: 1200px; overflow: hidden;
    background: var(--backdrop);
  }
  .stage {
    position: relative; width: 1200px; height: 1200px;
  }
  .card {
    position: absolute; left: 150px; width: 900px; height: 514px;
    background: var(--card);
    border: 1px solid var(--card-edge);
    box-shadow: 0 12px 30px rgba(0,0,0,0.45);
  }
  .card--back { top: 60px; }
  .card--front { top: 626px; }

  .back-wordmark {
    position: absolute; inset: 0;
    display: flex; align-items: center; justify-content: center;
    font-family: "Marcellus", serif;
    font-size: 52px; letter-spacing: 3px;
    color: var(--emboss);
    text-shadow: 1px 1px 0 var(--emboss-light);
  }

  .front-brand {
    position: absolute; left: 90px; top: 96px;
    font-family: "Marcellus", serif;
    font-size: 38px; letter-spacing: 1px;
    color: var(--teal);
  }
  .front-brand .tagline { display: block; font-size: 22px; margin-top: 6px; }

  .person { position: absolute; left: 90px; top: 236px; }
  .person__name {
    font-family: "Montserrat", sans-serif; font-weight: 600;
    font-size: 34px; color: var(--white); letter-spacing: 1px;
  }
  .person__role {
    font-family: "Roboto", sans-serif; font-size: 20px;
    color: var(--teal); margin-top: 2px;
  }

  .contacts {
    position: absolute; left: 90px; top: 340px;
    list-style: none;
    font-family: "Roboto", sans-serif; font-size: 20px;
    color: var(--grey-text); letter-spacing: 0.5px;
  }
  .contacts li { display: flex; align-items: center; height: 32px; }
  .contacts svg { width: 18px; height: 18px; margin-right: 12px; flex: none; }
</style>
</head>
<body>
<main class="stage">
  <section class="card card--back">
    <div class="back-wordmark">SUNNY KITE ACADEMY</div>
  </section>

  <section class="card card--front">
    <div class="front-brand">SUNNY KITE ACADEMY<span class="tagline">for Mandarin Learning</span></div>

    <div class="person">
      <div class="person__name">MIRA TOLLAN</div>
      <div class="person__role">Manager</div>
    </div>

    <ul class="contacts">
      <li>
        <svg viewBox="0 0 18 18" fill="none" stroke="#e0605e" stroke-width="1.6"><rect x="5" y="1.5" width="8" height="15" rx="1.5"/><line x1="8" y1="14" x2="10" y2="14"/></svg>
        000-000-0000
      </li>
      <li>
        <svg viewBox="0 0 18 18"><path fill="#e0605e" d="M4.5 2 L7 2 L8 5.5 L6.3 7 C7.3 9.2 8.8 10.7 11 11.7 L12.5 10 L16 11 L16 13.5 C16 14.9 14.9 16 13.5 16 C8.2 15.6 2.4 9.8 2 4.5 C2 3.1 3.1 2 4.5 2 Z"/></svg>
        000-000-0000
      </li>
      <li>
        <svg viewBox="0 0 18 18"><rect x="1.5" y="4" width="15" height="10" fill="#e0605e"/><path d="M1.5 4 L9 10 L16.5 4" fill="none" stroke="#1f2021" stroke-width="1.3"/></svg>
        info@sunnykiteacademy.com
      </li>
      <li>
        <svg viewBox="0 0 18 18" fill="none" stroke="#e0605e" stroke-width="1.4"><circle cx="9" cy="9" r="7"/><ellipse cx="9" cy="9" rx="3" ry="7"/><line x1="2" y1="9" x2="16" y2="9"/></svg>
        www.sunnykiteacademy.com
      </li>
    </ul>
  </section>
</main>
</body>
</html>
```